Maple Hollow Bloom Panels Business card

Looking to have a business card design incorporating my logo for my flower wall business.

Industry/Entity Type

Wedding & event planning

Contact Information for Business Card

My business logo, my name - Lena Whitcombe (owner), my tagline - Let us be your something extra, phone # 401-726-3148, email address - maplehollowbloompanels@mailvane.net, my website - maplehollowbloompanels.net, Instagram handle- @maplehollowbloompanels, FB handle Handle - maplehollowbloompanels

Font styles to use
Other font styles liked:
• Sentaina is the font that is used in my logo

Requirements
Must have
• Would like a double sided business card

```html
<!DOCTYPE html>
<html lang="en">
<head>
<meta charset="utf-8">
<title>Maple Hollow Bloom Panels – Business Card</title>
<link href="https://fonts.googleapis.com/css2?family=Montserrat:wght@400;600&display=swap" rel="stylesheet">
<style>
  :root {
    --page-bg: #d9d9d9;
    --card-white: #ffffff;
    --card-pink: #f9dfe9;
    --accent-pink: #d57aa8;
    --ink: #4a4a4a;
    --logo-ink: #2b2b2b;
    --gold: #d8b45a;
    --divider: #bdbdbd;
  }
  * { margin: 0; padding: 0; box-sizing: border-box; }
  html, body { width: 1200px; height: 1164px; overflow: hidden; }
  body {
    background: var(--page-bg);
    font-family: "Montserrat", sans-serif;
    color: var(--ink);
    position: relative;
  }
  .card {
    position: absolute;
    left: 160px;
    width: 880px;
    height: 500px;
    border-radius: 22px;
    box-shadow: 0 4px 14px rgba(0,0,0,0.18);
    overflow: hidden;
  }
  .card--front { top: 58px; background: var(--card-white); }
  .card--back { top: 606px; background: var(--card-pink); }

  .logo-mark {
    position: absolute;
    border-radius: 50%;
    display: flex;
    align-items: center;
    justify-content: center;
    text-align: center;
    font-family: "Montserrat", sans-serif;
    font-weight: 400;
    color: var(--logo-ink);
    letter-spacing: 0.04em;
  }
  .card--front .logo-mark {
    left: 125px; top: 133px; width: 210px; height: 210px;
    border: 2px solid var(--gold);
    font-size: 19px; line-height: 1.35;
  }
  .card--back .logo-mark {
    left: 277px; top: 91px; width: 330px; height: 330px;
    background: var(--card-white);
    font-size: 30px; line-height: 1.35;
  }

  .divider {
    position: absolute;
    left: 364px; top: 143px;
    width: 1px; height: 213px;
    background: var(--divider);
  }
  .details { position: absolute; left: 400px; top: 150px; }
  .details__name {
    font-weight: 600; font-size: 26px; color: var(--accent-pink);
    letter-spacing: 0.02em; text-transform: uppercase; line-height: 1.1;
  }
  .details__role { font-size: 19px; line-height: 1.3; }
  .contact-list { list-style: none; font-size: 19.5px; line-height: 25.5px; }
  .contact-list--social { margin-top: 20px; }
  .contact-list--direct { margin-top: 14px; }
  .contact-list li { display: flex; align-items: center; gap: 10px; white-space: nowrap; }
  .contact-list svg { width: 15px; height: 15px; flex: none; }
  .dot { width: 14px; height: 14px; border-radius: 50%; background: var(--accent-pink); flex: none; }

  .tagline {
    position: absolute; left: 0; width: 876px; top: 428px;
    text-align: center; font-size: 19.5px;
  }
</style>
</head>
<body>
  <section class="card card--front" aria-label="Card front">
    <div class="logo-mark">Maple Hollow<br>Bloom Panels</div>
    <div class="divider"></div>
    <div class="details">
      <p class="details__name">Lena Whitcombe</p>
      <p class="details__role">Owner</p>
      <ul class="contact-list contact-list--social">
        <li><span class="dot"></span>@maplehollowbloompanels</li>
        <li><span class="dot"></span>maplehollowbloompanels</li>
      </ul>
      <ul class="contact-list contact-list--direct">
        <li>
          <svg viewBox="0 0 16 16" aria-hidden="true"><path d="M4 1.5l2.5 3-1.6 1.6c.8 1.9 2.2 3.3 4 4l1.6-1.6 3 2.5-1.6 2.5C7 13 3 9 1.5 3.1z" fill="none" stroke="var(--accent-pink)" stroke-width="1.5" stroke-linejoin="round"/></svg>
          401-726-3148
        </li>
        <li>
          <svg viewBox="0 0 16 16" aria-hidden="true"><rect x="1" y="3" width="14" height="10" fill="var(--accent-pink)"/><path d="M1 3l7 6 7-6" fill="none" stroke="#fff" stroke-width="1.3"/></svg>
          maplehollowbloompanels@mailvane.net
        </li>
        <li>
          <svg viewBox="0 0 16 16" aria-hidden="true" fill="none" stroke="var(--accent-pink)" stroke-width="1.3"><circle cx="8" cy="8" r="6.5"/><ellipse cx="8" cy="8" rx="3" ry="6.5"/><path d="M1.5 8h13M2.5 4.7h11M2.5 11.3h11"/></svg>
          www.maplehollowbloompanels.net
        </li>
      </ul>
    </div>
    <p class="tagline">Let us be your something extra</p>
  </section>

  <section class="card card--back" aria-label="Card back">
    <div class="logo-mark">Maple Hollow<br>Bloom Panels</div>
  </section>
</body>
</html>
```